Tarjetas de visita para empresa de aluminio

Empresa con mas de 40 años vendiendo perfiles de aluminio.
Somos fábrica y almacén, queremos renovar la tarjeta de presentación de nuestros comerciales dando una imgen innovadora y tecnógica mezclado con la calidez del respeto al medio ambiente.
Añado el logo de la empresa y actual cara trasera de la tarjeta de visita, el logo es el simbolo WM y la marca TRAVENIC EXTRUSION, la frase 2extrusion y lacado de aluminio" debe cambiarse por "Diseño, extrusión, lacado, anodizado y mecanizado de precisión de aluminio" o en su defecto incluir todos esos servicios que hacemos o una frase mas pegadiza.

We are an aluminium factory, we produce and stock profiles of aluminium.
we want to renew visit card of our sellers, we are looking for something that show innovation, tecnology and environment respect.
Upload our actual logo and back of visit card, logo WM and brand TRAVENIC EXTRUSION must be keept.
Text "Extrusion y lacado de aluminio" must be changed for "Diseño, extrusion, lacado, anodizado y mecanizado de precisión de aluminio" or something like that

```html
<!DOCTYPE html>
<html lang="es">
<head>
<meta charset="utf-8">
<title>Travenic Extrusion – Tarjetas de visita</title>
<link href="https://fonts.googleapis.com/css2?family=Open+Sans:wght@400;600;700&display=swap" rel="stylesheet">
<style>
  :root {
    --page-bg: #eef1f5;
    --card-white: #ffffff;
    --navy: #0d2341;
    --brand-blue: #1a63d6;
    --mid-blue: #3f86e8;
    --light-blue: #c7dcf7;
    --text-dark: #2a2f38;
    --text-light: #ffffff;
    --text-muted: #c9d3e2;
  }
  * { box-sizing: border-box; margin: 0; padding: 0; }
  html, body { width: 1200px; height: 2316px; overflow: hidden; }
  body {
    background: var(--page-bg);
    font-family: "Open Sans", Arial, sans-serif;
    display: flex;
    flex-direction: column;
    align-items: center;
    justify-content: center;
    gap: 120px;
  }
  .card {
    position: relative;
    width: 1000px;
    height: 520px;
    overflow: hidden;
    box-shadow: 0 18px 40px rgba(13, 35, 65, 0.18);
  }
  .card-front { background: var(--card-white); }
  .card-back { background: var(--navy); color: var(--text-light); }
  .front-waves { position: absolute; inset: 0; width: 100%; height: 100%; }

  .brand {
    position: absolute;
    display: flex;
    flex-direction: column;
    align-items: center;
    text-align: center;
  }
  .brand-dot {
    width: 110px; height: 110px;
    border-radius: 50%;
    border: 9px solid var(--brand-blue);
    margin-bottom: 22px;
  }
  .brand-name {
    font-weight: 700;
    color: var(--brand-blue);
    letter-spacing: 3px;
    white-space: nowrap;
  }
  .brand-tagline {
    font-weight: 400;
    letter-spacing: 1px;
    margin-top: 8px;
    text-transform: uppercase;
    line-height: 1.45;
  }
  .card-front .brand { left: 0; right: 0; top: 80px; }
  .card-front .brand-name { font-size: 42px; }
  .card-front .brand-tagline { font-size: 16px; color: var(--brand-blue); }
  .website {
    position: absolute;
    left: 0; right: 0; top: 450px;
    text-align: center;
    font-size: 24px;
    letter-spacing: 2.5px;
    color: var(--text-dark);
  }

  .person { position: absolute; left: 65px; top: 58px; }
  .person-name {
    font-size: 44px;
    font-weight: 700;
    line-height: 1.45;
    text-transform: uppercase;
  }
  .person-role {
    font-size: 17px;
    letter-spacing: 1px;
    text-transform: uppercase;
    color: var(--text-muted);
    margin-top: 4px;
  }
  .card-back .brand { left: 490px; width: 460px; top: 95px; }
  .card-back .brand-dot { width: 80px; height: 80px; border-width: 7px; margin-bottom: 14px; }
  .card-back .brand-name { font-size: 30px; letter-spacing: 2px; }
  .card-back .brand-tagline { font-size: 13px; color: var(--text-light); }

  .contact {
    position: absolute;
    display: flex;
    align-items: flex-start;
    gap: 30px;
    font-size: 17px;
    font-weight: 600;
    line-height: 1.55;
  }
  .contact svg { flex: none; width: 32px; height: 32px; fill: var(--text-light); }
  .contact-phone { left: 80px; top: 350px; }
  .contact-mail { left: 80px; top: 458px; align-items: center; }
  .contact-address { left: 465px; top: 350px; }
  .contact-web { left: 465px; top: 458px; align-items: center; }
</style>
</head>
<body>

  <section class="card card-front" aria-label="Cara frontal">
    <svg class="front-waves" viewBox="0 0 1000 520" preserveAspectRatio="none" aria-hidden="true">
      <path d="M0 300 C 60 420, 220 500, 520 520 L 0 520 Z" fill="var(--mid-blue)"/>
      <path d="M60 0 C -40 180, 80 420, 520 520 L 0 520 L 0 0 Z" fill="var(--light-blue)"/>
      <path d="M0 380 C 90 470, 260 515, 420 520 L 0 520 Z" fill="var(--brand-blue)"/>
      <path d="M1000 240 C 960 400, 820 490, 640 520 L 1000 520 Z" fill="var(--light-blue)"/>
      <path d="M1000 330 C 950 430, 860 495, 720 520 L 1000 520 Z" fill="var(--mid-blue)"/>
      <path d="M1000 420 C 960 480, 900 510, 820 520 L 1000 520 Z" fill="var(--brand-blue)"/>
    </svg>
    <div class="brand">
      <div class="brand-dot"></div>
      <div class="brand-name">TRAVENIC EXTRUSION</div>
      <div class="brand-tagline">Diseño, extrusión, lacado, anodizado y mecanizado de precisión de aluminio</div>
    </div>
    <div class="website">www.travenic.com</div>
  </section>

  <section class="card card-back" aria-label="Cara trasera">
    <div class="person">
      <div class="person-name">Marcos Delgado<br>Ruiz</div>
      <div class="person-role">Commercial</div>
    </div>
    <div class="brand">
      <div class="brand-dot"></div>
      <div class="brand-name">TRAVENIC EXTRUSION</div>
      <div class="brand-tagline">Diseño, extrusión, lacado, anodizado<br>y mecanizado de precisión de aluminio</div>
    </div>

    <div class="contact contact-phone">
      <svg viewBox="0 0 24 24" aria-hidden="true"><path d="M6.6 10.8a15.1 15.1 0 0 0 6.6 6.6l2.2-2.2c.3-.3.7-.4 1-.2 1.1.4 2.3.6 3.6.6.6 0 1 .4 1 1V20c0 .6-.4 1-1 1A17 17 0 0 1 3 4c0-.6.4-1 1-1h3.5c.6 0 1 .4 1 1 0 1.3.2 2.5.6 3.6.1.3 0 .7-.2 1z"/></svg>
      <div>(Movil) 600 41 27 58<br>(Telf) 900 52 14 36<br>(Fax) 900 52 14 37</div>
    </div>
    <div class="contact contact-mail">
      <svg viewBox="0 0 24 24" aria-hidden="true"><path d="M3 5h18v14H3z M3 5l9 7 9-7" fill="var(--text-light)" stroke="var(--navy)" stroke-width="1.4"/></svg>
      <div>mdelgado@travenic.com</div>
    </div>
    <div class="contact contact-address">
      <svg viewBox="0 0 24 24" aria-hidden="true"><path d="M12 2a7 7 0 0 0-7 7c0 5.2 7 13 7 13s7-7.8 7-13a7 7 0 0 0-7-7zm0 9.5A2.5 2.5 0 1 1 12 6.5a2.5 2.5 0 0 1 0 5z"/></svg>
      <div>Pol. Ind. Norte - C/ 4 N 12 ,<br>41000 VILLANUEVA (Sevilla),<br>Apartado de Correos 210</div>
    </div>
    <div class="contact contact-web">
      <svg viewBox="0 0 24 24" aria-hidden="true"><circle cx="12" cy="12" r="10"/><path d="M2 12h20M12 2c3 3 3 17 0 20M12 2c-3 3-3 17 0 20M4 7h16M4 17h16" fill="none" stroke="var(--navy)" stroke-width="1.2"/></svg>
      <div>www.travenic.com</div>
    </div>
  </section>

</body>
</html>
```